Postcard Design hearing aid sales & service. Free hearing test . Fresh batteries

Cedar Hollow Hearing Aid Device Center . Located at 417 Marlowe Ln Abilene Texas 79605 Ph 325-555-0148.
Hours Mon thru Thurs 9:00am - 5:00pm closed for lunch 12:00pm - 1:00pm . Fri open 9:00am - 1:00pm
Hearing Test n/c Hearing aid adjustment & cleaning of hearing aids n/c . Fresh batteries buy one 1/2 off on 2nd pack. Limited time. Walk-in welcome Appointments appreciated. THIS MONTH ONLY Special discounts on new state of the art hearing aids w/remote. .

```html
<!DOCTYPE html>
<html lang="en">
<head>
<meta charset="utf-8">
<title>Cedar Hollow Hearing Aid Device Center – Postcard</title>
<link rel="stylesheet" href="https://fonts.googleapis.com/css2?family=Lato:wght@400;700;900&family=Roboto+Condensed:wght@400;700&family=Roboto:wght@700;900&display=swap">
<style>
  :root {
    --teal: #4bc1b8;
    --pink: #c44d7c;
    --charcoal: #3a3b3d;
    --ink: #1f1f21;
    --paper: #ffffff;
    --stage: #e9e6e1;
    --stamp: #8a8b8c;
    --rule: #9a9a9a;
  }
  * { box-sizing: border-box; margin: 0; padding: 0; }
  html, body { width: 907px; height: 1200px; overflow: hidden; }
  body { background: var(--stage); position: relative; font-family: "Lato", sans-serif; color: var(--ink); }

  .card { position: absolute; left: 110px; width: 690px; overflow: hidden; box-shadow: 0 3px 10px rgba(0,0,0,.25); }
  .card--front { top: 45px; height: 533px; background: linear-gradient(#f6f6f6, #e4e4e4); }
  .card--back { top: 600px; height: 535px; background: var(--paper); }

  .shapes { position: absolute; inset: 0; }

  /* front */
  .brand { position: absolute; left: 38px; top: 36px; font-family: "Roboto", sans-serif; font-weight: 900; font-size: 28px; letter-spacing: .5px; color: var(--charcoal); }
  .welcome-band { position: absolute; left: 0; top: 82px; width: 100%; height: 88px; background: var(--charcoal); border-top: 4px solid var(--pink); border-bottom: 4px solid var(--pink); }
  .welcome-band h1 { position: absolute; left: 0; width: 300px; top: 8px; text-align: center; font-family: "Roboto Condensed", sans-serif; font-weight: 700; font-size: 37px; color: var(--teal); letter-spacing: .5px; }
  .welcome-band p { position: absolute; left: 0; width: 300px; top: 53px; text-align: center; font-family: "Roboto Condensed", sans-serif; font-weight: 700; font-size: 13.5px; color: var(--paper); text-transform: uppercase; white-space: nowrap; }
  .hours-band { position: absolute; left: 0; top: 194px; width: 100%; height: 146px; background: var(--teal); border-top: 4px solid var(--charcoal); border-bottom: 4px solid var(--charcoal); text-align: center; }
  .hours-band .inner { width: 318px; padding-top: 10px; }
  .hours-band h2 { font-family: "Roboto Condensed", sans-serif; font-weight: 700; font-size: 21px; color: var(--pink); line-height: 24px; }
  .hours-band p { font-weight: 900; font-size: 18px; line-height: 21px; color: var(--ink); white-space: nowrap; }
  .hours-band p.note { font-size: 16px; }
  .service-title { position: absolute; left: 104px; top: 350px; font-weight: 700; font-size: 20px; color: var(--pink); }
  .services { position: absolute; top: 390px; list-style: none; font-size: 13.5px; line-height: 17px; color: var(--ink); }
  .services li { position: relative; padding-left: 12px; }
  .services li::before { content: ""; position: absolute; left: 0; top: 6px; width: 6px; height: 6px; border-radius: 50%; background: var(--teal); }
  .services--a { left: 30px; }
  .services--b { left: 210px; top: 392px; }
  .phone-line { position: absolute; left: 36px; top: 482px; display: flex; align-items: center; gap: 8px; font-family: "Roboto Condensed", sans-serif; font-weight: 700; font-size: 27px; color: var(--paper); }

  /* back */
  .story-title { position: absolute; left: 28px; top: 24px; font-weight: 900; font-size: 16px; color: var(--pink); }
  .story { position: absolute; left: 33px; top: 60px; width: 352px; font-size: 13.3px; line-height: 18.3px; text-align: justify; color: var(--ink); }
  .thumb { position: absolute; top: 213px; width: 131px; height: 125px; border: 4px solid var(--pink); border-radius: 4px; }
  .thumb--hand { left: 35px; background: linear-gradient(135deg, #cfe6ee, #e6b9a6 55%, #f1dcd2); }
  .thumb--consult { left: 187px; background: linear-gradient(135deg, #f2e7df, #d9b49f 50%, #8fb6d4); }
  .stamp { position: absolute; left: 625px; top: 18px; width: 48px; height: 50px; background: var(--stamp); }
  .address-rule { position: absolute; left: 480px; width: 145px; height: 1px; background: var(--rule); }
  .contacts { position: absolute; left: 33px; top: 442px; list-style: none; font-weight: 700; font-size: 17.5px; line-height: 22.5px; color: var(--ink); }
  .contacts li { display: flex; align-items: center; gap: 8px; }
  .contacts svg { width: 14px; height: 14px; }
</style>
</head>
<body>

<section class="card card--front" aria-label="Postcard front">
  <div class="brand">YOUR LOGO</div>
  <div class="welcome-band">
    <h1>WELCOME TO</h1>
    <p>Cedar Hollow Hearing Aid Device Center</p>
  </div>
  <div class="hours-band">
    <div class="inner">
      <h2>OPEN HOURS</h2>
      <p>Monday toThursday</p>
      <p>9:00am - 5:00pm</p>
      <p class="note">(closed for lunch 12:00pm - 1:00pm)</p>
      <p>Fri open 9:00am - 1:00pm</p>
    </div>
  </div>

  <svg class="shapes" width="690" height="533" viewBox="0 0 690 533">
    <defs>
      <linearGradient id="photoTone" x1="0" y1="0" x2="1" y2="1">
        <stop offset="0" stop-color="#e4ddd6"/>
        <stop offset=".45" stop-color="#c9b7aa"/>
        <stop offset=".8" stop-color="#3f7fa0"/>
        <stop offset="1" stop-color="#d9d4cf"/>
      </linearGradient>
    </defs>
    <path d="M0 455 C 180 440 360 440 520 533 L0 533 Z" fill="#3a3b3d"/>
    <path d="M0 450 C 200 432 390 436 560 533 L520 533 C 360 440 180 440 0 455 Z" fill="#c44d7c"/>
    <path d="M370 392 C 420 392 470 410 640 533 L605 533 C 480 445 430 420 370 405 Z" fill="#c44d7c"/>
    <path d="M288 0 C 318 240 450 450 660 533 L690 533 L690 0 Z" fill="#4bc1b8"/>
    <path d="M300 0 C 330 235 460 445 690 520 L690 0 Z" fill="#3a3b3d"/>
    <g role="img" aria-label="Photo: a caregiver fitting a hearing aid behind an older woman's ear">
      <path d="M306 0 C 336 232 466 440 690 512 L690 0 Z" fill="url(#photoTone)"/>
    </g>
  </svg>

  <div class="service-title">our service</div>
  <ul class="services services--a">
    <li>Hearing Test n/c</li>
    <li>Hearing aid adjustment &amp;<br>cleaning of hearing aids n/c</li>
  </ul>
  <ul class="services services--b">
    <li>Fresh batteries buy one<br>1/2 off on 2nd pack</li>
  </ul>
  <div class="phone-line">
    <svg width="26" height="26" viewBox="0 0 26 26" aria-hidden="true">
      <circle cx="13" cy="13" r="11.5" fill="none" stroke="#4bc1b8" stroke-width="2"/>
      <path d="M9 7.5 l2.5 -.5 1.3 3 -1.6 1.2 c.8 1.7 1.9 2.8 3.6 3.6 l1.2 -1.6 3 1.3 -.5 2.5 c-5.5 .3 -9.8 -4 -9.5 -9.5z" fill="#4bc1b8"/>
    </svg>
    <span>325-555-0148</span>
  </div>
</section>

<section class="card card--back" aria-label="Postcard back">
  <svg class="shapes" width="690" height="535" viewBox="0 0 690 535">
    <defs>
      <linearGradient id="fadeTone" x1="0" y1="0" x2="1" y2="1">
        <stop offset="0" stop-color="#f3f1f2"/>
        <stop offset=".5" stop-color="#eef0f3"/>
        <stop offset="1" stop-color="#fafafa"/>
      </linearGradient>
    </defs>
    <g role="img" aria-label="Faded photo of a hearing specialist with a patient">
      <path d="M0 0 L400 0 C 430 90 440 230 380 300 C 310 380 150 405 0 405 Z" fill="url(#fadeTone)"/>
    </g>
    <path d="M400 0 C 430 90 440 230 380 300 C 310 380 150 405 0 405" fill="none" stroke="#4bc1b8" stroke-width="10"/>
    <path d="M410 0 C 440 95 448 235 386 306 C 316 386 150 412 0 412" fill="none" stroke="#3a3b3d" stroke-width="2"/>
    <path d="M442 160 C 444 255 405 330 325 375 C 235 420 110 425 0 425" fill="none" stroke="#c44d7c" stroke-width="10"/>
  </svg>

  <h2 class="story-title">OUR STORY</h2>
  <p class="story">Cedar Hollow Hearing Aid Device Center is located at 417 Marlowe Ln, Abilene, Texas 79605. Hearing tests, hearing aid adjustment and cleaning of hearing aids are offered at no charge. Fresh batteries: buy one, get 1/2 off the 2nd pack for a limited time. Walk-ins welcome, appointments appreciated. THIS MONTH ONLY: special discounts on new state of the art hearing aids with remote.</p>

  <div class="thumb thumb--hand" role="img" aria-label="Photo: a hearing aid resting in an open hand"></div>
  <div class="thumb thumb--consult" role="img" aria-label="Photo: a specialist handing a hearing aid to a patient over a clipboard"></div>

  <div class="stamp" aria-label="Stamp area"></div>
  <div class="address-rule" style="top:213px"></div>
  <div class="address-rule" style="top:243px"></div>
  <div class="address-rule" style="top:267px"></div>

  <ul class="contacts">
    <li>
      <svg viewBox="0 0 14 14" aria-hidden="true"><circle cx="7" cy="7" r="6" fill="none" stroke="#c44d7c" stroke-width="1.3"/><path d="M4.8 4 l1.3-.3 .7 1.6 -.9.7 c.4.9 1 1.5 1.9 1.9 l.7-.9 1.6.7 -.3 1.3 c-2.9.2-5.2-2.1-5-5z" fill="#c44d7c"/></svg>
      <span>325-555-0148</span>
    </li>
    <li>
      <svg viewBox="0 0 14 14" aria-hidden="true"><circle cx="7" cy="7" r="5.8" fill="#c44d7c"/><path d="M1.5 7 h11 M7 1.2 v11.6 M7 1.2 c-3 3-3 8.6 0 11.6 M7 1.2 c3 3 3 8.6 0 11.6" stroke="#fff" stroke-width=".9" fill="none"/></svg>
      <span>www.cedarhollowhearing.com</span>
    </li>
    <li>
      <svg viewBox="0 0 14 14" aria-hidden="true"><rect x="1" y="3" width="12" height="8.5" fill="#c44d7c"/><path d="M1 3 l6 5 6-5" stroke="#fff" stroke-width="1" fill="none"/></svg>
      <span>info@cedarhollowhearing.com</span>
    </li>
  </ul>
</section>

</body>
</html>
```